Maple Cove Laser Dermal Studio needs an 8 page WP redesign

We need a colorful re-design for an 8 page Wordpress website. The current preliminary website is live. The home page URL is http://maplecovelaserdermalstudio.com The new logo is live on the website also. I would like a (re)design using the colors that are represented by the new logo file, and any additional complimentary colors. The information regarding the business can be found on the website already, so please review it for insight. The name of the business is "Maple Cove Laser Dermal Studio".

Target Market(s)

The targeted website viewer is an adult female between the ages of 30 and 75 who is interested in facial renewal, wart removal and scar removal. This website should inspire in the target viewer the benefits of laser facial renewal, wart removal and new scar removal. Potential website viewers are wanting and searching for improved skin health and appearance. The website must represent the essence of a professional spa business.

Industry/Entity Type

Business

Font styles to use
Sans Serif

Requirements
Must have
• - The phone number placed in a visible and high value widget area that allows mobile phone browser dialing.

```html
<!DOCTYPE html>
<html lang="en">
<head>
<meta charset="utf-8">
<title>Maple Cove Laser Dermal Studio</title>
<link rel="stylesheet" href="https://fonts.googleapis.com/css2?family=Roboto:wght@300;400;500;700&display=swap">
<style>
:root{
  --plum-dark:#2a0f27;
  --plum-deep:#1f0a1d;
  --violet:#7a2fb8;
  --violet-box:#8a3fc6;
  --magenta:#b43fb0;
  --pink:#e2418c;
  --hot-pink:#e83c8f;
  --text:#4a4a4a;
  --muted:#8a8a8a;
  --field:#e6e8ec;
  --white:#fff;
}
*{box-sizing:border-box;margin:0;padding:0}
html,body{width:770px;height:1200px;overflow:hidden}
body{position:relative;font-family:"Roboto",Arial,sans-serif;color:var(--text);background:#e4e4e6}
a{color:inherit;text-decoration:none}
.abs{position:absolute}

/* header */
.site-header{position:absolute;left:0;top:0;width:770px;height:41px;background:var(--plum-dark)}
.brand{position:absolute;left:154px;top:8px;width:130px;color:var(--white);font-weight:500;font-size:10.5px;line-height:12px;display:flex;align-items:center;gap:6px}
.brand-mark{width:16px;height:16px;border-radius:50%;background:var(--hot-pink);flex:none}
.main-nav{position:absolute;right:151px;top:6px;display:flex;gap:13px;font-size:6px;color:var(--white);text-transform:uppercase}
.main-nav a{padding:2px 0}
.main-nav a.active{border:1px solid var(--magenta);padding:2px 5px;color:#f1c9ee}
.header-contact{position:absolute;right:151px;top:23px;font-size:5.4px;color:var(--white);text-align:right;line-height:7.5px}
.header-contact .lbl{color:var(--hot-pink)}

/* hero */
.hero{position:absolute;left:0;top:41px;width:770px;height:259px;overflow:hidden;
  background:radial-gradient(circle at 70% 45%,#f3d9d3 0 18%,transparent 40%),linear-gradient(90deg,#f6f0f2 0%,#f4c9de 30%,#eedad6 62%,#f4b7d2 100%)}
.hero-photo{position:absolute;inset:0}
.hero-copy{position:absolute;left:154px;top:60px;width:250px}
.hero-title{font-weight:300;font-size:17px;line-height:17px;color:var(--magenta)}
.hero-text{margin-top:7px;font-size:6.8px;line-height:10.5px;color:#333}
.btn{display:inline-block;background:var(--magenta);color:var(--white);font-size:5.8px;font-weight:500;text-transform:uppercase}
.hero .btn{margin-top:9px;width:49px;height:16px;line-height:16px;text-align:center}
.slider-dots{position:absolute;left:373px;top:241px;display:flex;gap:4px}
.slider-dots span{width:6px;height:6px;border-radius:50%;border:1px solid var(--magenta)}
.slider-dots span.on{background:var(--magenta)}

/* main */
.main{position:absolute;left:0;top:300px;width:770px;height:630px;background:radial-gradient(ellipse at 40% 30%,#fafafa 0%,#ececee 55%,#d5d5d8 100%)}
.content{position:absolute;left:154px;top:10px;width:264px}
.section-title{position:relative;padding-left:10px;font-weight:300;font-size:14.5px;line-height:17px;color:#333}
.section-title::before{content:"";position:absolute;left:0;top:1px;width:3px;height:15px;background:var(--magenta)}
.content p{font-size:5.9px;line-height:8.1px;color:#555}
.content p + p{margin-top:7px}
.content a.link{color:var(--violet);text-decoration:underline}
.sub-title{font-size:8.2px;font-weight:400;color:var(--pink);margin:11px 0 4px}
.media{display:flex;gap:7px;margin-top:10px}
.media-img{flex:none;width:72px}
.img-portrait{height:104px;background:linear-gradient(160deg,#d9c5b8,#8d6e5e 55%,#3b2620)}
.img-device{height:94px;background:linear-gradient(160deg,#eef0f0,#b9bdbf 50%,#6f7476)}
.caption{font-size:5.6px;font-style:italic;color:var(--violet);margin-top:8px}

/* sidebar */
.sidebar{position:absolute;left:430px;top:0;width:159px}
.promo-head{position:relative;height:90px}
.promo-photo{position:absolute;left:50px;top:0;width:108px;height:90px;border-radius:40px 40px 0 0;background:linear-gradient(170deg,#3a2826 0%,#d8b5a4 45%,#efd9cf 100%)}
.promo-title{position:absolute;left:6px;top:36px;font-weight:300;font-size:13.5px;line-height:14.5px;color:var(--magenta)}
.promo-box{width:159px;height:144px;background:linear-gradient(180deg,var(--violet-box),#6c2ab0);color:var(--white);padding:7px 0 0;box-shadow:0 2px 4px rgba(0,0,0,.25)}
.promo-box h3{font-size:9px;font-weight:700;padding:0 6px}
.promo-box .note{font-size:5.8px;line-height:7px;color:#e4d3f3;padding:0 6px;margin-top:4px}
.promo-box .ends{font-size:7.2px;padding:0 6px;margin-top:5px}
.deal{display:flex;align-items:center;height:15px;margin-top:4px;font-size:8px}
.deal b.num{width:20px;height:15px;line-height:15px;text-align:center;background:var(--hot-pink);font-size:10px;margin-right:5px}
.deal strong{margin-left:3px}
.promo-call{padding:0 6px;margin-top:6px;font-size:9.5px;line-height:10px}
.promo-call a{font-weight:700}
.promo-call small{display:block;font-size:5.8px;color:#e4d3f3}
.blog-title{margin-top:18px;padding-left:6px;font-weight:300;font-size:13.5px;color:var(--magenta)}
.blog-sub{padding-left:6px;font-size:7px;color:#444;text-transform:uppercase}
.post{position:relative;width:159px;height:117px;background:var(--white);margin-top:6px;box-shadow:0 1px 3px rgba(0,0,0,.2)}
.post + .post{height:120px;margin-top:4px}
.post-img{position:absolute;left:0;top:0;width:74px;height:100%}
.post-img.one{background:linear-gradient(160deg,#c9d5b3,#e9c9b0 50%,#b79a88)}
.post-img.two{background:linear-gradient(160deg,#d7d9dc,#e8cbb8 50%,#9c8f90)}
.post-body{position:absolute;left:80px;top:8px;width:74px}
.post-date{font-size:5.8px;color:var(--pink);font-weight:500}
.post-title{font-size:7px;font-weight:700;line-height:8.5px;color:#333;margin-top:3px}
.post-text{font-size:5.2px;line-height:6.6px;color:#777;margin-top:3px}
.post-actions{position:absolute;left:58px;bottom:3px;display:flex}
.post-actions span{width:16px;height:15px;background:#8d8d8d;display:flex;align-items:center;justify-content:center}
.post-actions span + span{background:#bdbdbd}
.post .btn{position:absolute;right:0;bottom:3px;width:37px;height:15px;line-height:15px;text-align:center;background:var(--violet)}

/* appointment */
.appointment{position:absolute;left:148px;top:930px;width:474px;height:200px;background:linear-gradient(90deg,#f4e7da 0%,#f2ddc6 60%,#eed2b4 100%);box-shadow:0 2px 5px rgba(0,0,0,.25)}
.appt-photo{position:absolute;left:0;top:0;width:116px;height:200px;background:linear-gradient(90deg,#d8b9a2,#f0d9c8 60%,#f3e5d8)}
.appt-info{position:absolute;left:120px;top:19px;width:120px}
.appt-head{position:relative;padding-left:6px}
.appt-head::before{content:"";position:absolute;left:0;top:2px;width:3px;height:13px;background:var(--magenta)}
.appt-head small{display:block;font-size:7px;color:#555;line-height:7px}
.appt-head strong{display:block;font-size:13.5px;font-weight:300;color:#222;line-height:13px;text-transform:uppercase}
.appt-info .lead{font-size:6px;line-height:8px;color:#222;margin:6px 0 0 10px}
.contact-title{margin-top:15px;font-size:13px;font-weight:300;color:var(--magenta)}
.contact-name{font-size:8px;color:#222;margin-top:2px}
.contact-line{font-size:6.2px;line-height:7.8px;color:#222;margin-top:2px}
.contact-line .lbl{color:var(--pink);display:block;margin-top:5px}
.booking{position:absolute;left:243px;top:20px;width:225px;height:162px;background:var(--white);padding:13px 13px 0;box-shadow:0 1px 3px rgba(0,0,0,.15)}
.booking .row{display:flex;gap:7px;margin-bottom:9px}
.field{flex:1}
.field label{display:block;font-size:5.4px;color:var(--muted);text-transform:uppercase;margin-bottom:4px}
.field .input{height:17px;background:var(--field)}
.field .area{height:36px;background:var(--field)}
.booking .btn{width:60px;height:15px;line-height:15px;text-align:center;background:var(--violet);margin-top:-2px}

/* footer */
.site-footer{position:absolute;left:0;top:1144px;width:770px;height:56px;background:var(--plum-dark)}
.site-footer .brand{top:10px}
.foot-nav{position:absolute;right:154px;top:9px;font-size:5.8px;color:var(--white);display:flex;gap:6px}
.foot-nav i{color:#8a6a85;font-style:normal}
.foot-contact{position:absolute;right:154px;top:24px;font-size:5.4px;color:var(--white)}
.foot-contact .lbl{color:var(--hot-pink)}
.copyright{position:absolute;left:0;bottom:0;width:770px;height:16px;line-height:16px;background:var(--plum-deep);text-align:center;font-size:4.8px;color:#9a8a98}
</style>
</head>
<body>

<header class="site-header">
  <a class="brand" href="http://maplecovelaserdermalstudio.com"><span class="brand-mark"></span><span>Maple Cove Laser Dermal Studio</span></a>
  <nav class="main-nav">
    <a class="active" href="#">About Us</a><a href="#">Skin Renewal</a><a href="#">Scar Removal</a><a href="#">Wart Removal</a><a href="#">Your Visit</a><a href="#">Contact Us</a><a href="#">Blog</a>
  </nav>
  <div class="header-contact">
    <span class="lbl">Phone:</span> <a href="tel:5553104827">(555) 310-4827</a><br>
    <span class="lbl">Email:</span> info@maplecovelaserdermalstudio.com
  </div>
</header>

<section class="hero">
  <div class="hero-photo" role="img" aria-label="Woman blowing pink rose petals from her hands, soft pink background"></div>
  <div class="hero-copy">
    <h1 class="hero-title">Are there any<br>Side Effects of<br>Laser Skin<br>Renewal Therapy?</h1>
    <p class="hero-text">You may experience some redness in the area after laser skin renewal therapy. However, it will not keep you away from your normal activities, as it will disappear after a few hours.</p>
    <a class="btn" href="#">View More</a>
  </div>
  <div class="slider-dots"><span></span><span class="on"></span><span></span></div>
</section>

<main class="main">
  <article class="content">
    <h2 class="section-title">Have you considered Laser Skin<br>Renewal Therapy?</h2>
    <div class="media">
      <div class="media-img img-portrait" role="img" aria-label="Portrait of a woman with smooth skin"></div>
      <div>
        <p>You will truly love laser skin renewal if your skin is showing signs of premature aging or the skin has sustained sun damage. Conditions such as excessive redness due to sun exposure or fine lines will be concerns of the past. In fact, <a class="link" href="#">laser skin therapy</a> is a unique and innovative way to enjoy youthful and healthy skin without resorting to painful and inconvenient surgery. Both men and women are receiving benefits from laser skin therapy.</p>
        <p>The literature contains ample scientific evidence to support laser skin renewal. After this therapy, your skin will produce collagen, which reduces and minimizes the appearance of fine lines and wrinkles. Imagine getting all this with minimal pain and no downtime? Doesn't it make you feel like getting in touch with our laser skin specialist today?</p>
      </div>
    </div>

    <h3 class="sub-title" style="margin-top:18px">Laser Skin Renewal is Innovative and Unique</h3>
    <p><a class="link" href="#">Laser skin therapy</a> is a non-invasive procedure that is extremely safe and effective. Above all, it is discrete and you never have to worry about family, friends and acquaintances, finding out that you have had treatment for fine lines and wrinkles.</p>
    <p>After each treatment, you will notice subtle but definite results. You will never have to hide indoors to wait for the skin irritation or bruising to disappear. The treatment sessions are comfortable and there is no worry about using topical anesthetic gels.</p>
    <p class="caption">Seeing is Believing...</p>
    <div class="media">
      <div class="media-img img-device" role="img" aria-label="Laser skin treatment machine"></div>
      <div>
        <p>Laser skin renewal does produce outstanding results. After mere five treatment sessions, you will notice a youthful glow about your skin and you also will find your skin looking smooth with an even tone.</p>
        <p>People, who have undergone <a class="link" href="#">laser treatment</a>, also find their complexion is healthier and creamier in appearance. Furthermore, you will find the size of large pore reduced to a significant extent and even minor imperfections on your face will not be as noticeable.</p>
        <p>While you may notice subtle changes and results after a single treatment, when you combine the results of multiple treatments, the results can be dramatic and startling.</p>
      </div>
    </div>

    <h3 class="sub-title" style="margin-top:18px">How Does Laser Skin Renewal-Therapy Work?</h3>
    <p>You are not the only one to ask this question, as many people have a misconception that the treatments are painful.</p>
    <p>When you have laser skin renewal session, your skin will be gently heated with the laser and this helps to stimulate production of collagen. The heating occurs in the upper dermal layer of your skin and this also dilates capillaries that help to reduce redness of your skin.</p>
    <p>Most people undergoing this treatment claim it is relaxing and soothing, without any discomfort or pain. Once your skin produces collagen, it will reduce the signs of wrinkles and fine lines.</p>

    <h3 class="sub-title" style="margin-top:15px">Number of Treatments</h3>
    <p>On an average, most people require anywhere from four to six treatments to get the best results. However, it must be noted that every person is different and has different needs. So, results will vary based on this. It is best to consult the <a class="link" href="#">therapist</a> to find out how many treatment sessions you will need for optimal results.</p>

    <h3 class="sub-title" style="margin-top:19px">Are there any Side Effects of Laser Skin Renewal Therapy?</h3>
    <p>You may experience some redness in the area after laser skin renewal therapy. However, it will not keep you away from your normal activities, as it will disappear after a few hours. The only caveat is applying SPF30 or more sunscreen when venturing outdoors. This will protect your treated skin from the sun which can mar the results of the treatment.</p>
    <p>Now that you know everything about <a class="link" href="#">laser skin renewal</a> therapy, what are you going to do about your fine lines and wrinkles?</p>
  </article>

  <aside class="sidebar">
    <div class="promo-head">
      <div class="promo-photo" role="img" aria-label="Smiling woman with hand on her cheek"></div>
      <h2 class="promo-title">New Years<br>Resolution<br>Special!</h2>
    </div>
    <div class="promo-box">
      <h3>Restore your youthful skin this year!</h3>
      <p class="note">Take advantage of our laser skin renewal specials for single or multiple sessions at low pricing.</p>
      <p class="ends">Special ENDS January 3, 2015 at 5:00 PM.</p>
      <div class="deal"><b class="num">1</b>SINGLE SESSION DEAL - <strong>$199</strong></div>
      <div class="deal"><b class="num">3</b>SESSIONS PACKAGE DEAL - <strong>$549</strong></div>
      <div class="deal"><b class="num">9</b>SESSIONS PACKAGE DEAL - <strong>$899</strong></div>
      <p class="promo-call">Call <a href="tel:5553104827">555-310-4827</a> to schedule<small>your convenient appointment.</small></p>
    </div>

    <h2 class="blog-title">Our Blog</h2>
    <p class="blog-sub">Recent Posts</p>
    <div class="post">
      <div class="post-img one" role="img" aria-label="Woman holding a lemon slice over one eye"></div>
      <div class="post-body">
        <p class="post-date">DEC 31,2014</p>
        <h4 class="post-title">The Benefits of Laser Skin Rejuvenation</h4>
        <p class="post-text">Laser skin renewal does produce outstanding results. After mere five treatment sessions, you will notice a youthful glow about your skin and you also will find your skin looking smooth with an even tone.</p>
      </div>
      <div class="post-actions">
        <span><svg width="7" height="7" viewBox="0 0 10 10"><circle cx="4" cy="4" r="3" fill="none" stroke="#fff" stroke-width="1.5"/><line x1="6.2" y1="6.2" x2="9" y2="9" stroke="#fff" stroke-width="1.6"/></svg></span>
        <span><svg width="8" height="7" viewBox="0 0 10 9"><path d="M5 9 1 5A2.3 2.3 0 0 1 5 1.6 2.3 2.3 0 0 1 9 5Z" fill="#fff"/></svg></span>
      </div>
      <a class="btn" href="#">Read</a>
    </div>
    <div class="post">
      <div class="post-img two" role="img" aria-label="Woman receiving a laser facial treatment"></div>
      <div class="post-body">
        <p class="post-date">DEC 26,2014</p>
        <h4 class="post-title">Laser Skin Renewal is Innovative and Unique</h4>
        <p class="post-text">Laser skin therapy is a non-invasive procedure that is extremely safe and effective. Above all, it is discrete and you never have to worry about family.</p>
      </div>
      <div class="post-actions">
        <span><svg width="7" height="7" viewBox="0 0 10 10"><circle cx="4" cy="4" r="3" fill="none" stroke="#fff" stroke-width="1.5"/><line x1="6.2" y1="6.2" x2="9" y2="9" stroke="#fff" stroke-width="1.6"/></svg></span>
        <span><svg width="8" height="7" viewBox="0 0 10 9"><path d="M5 9 1 5A2.3 2.3 0 0 1 5 1.6 2.3 2.3 0 0 1 9 5Z" fill="#fff"/></svg></span>
      </div>
      <a class="btn" href="#">Read</a>
    </div>
  </aside>
</main>

<section class="appointment">
  <div class="appt-photo" role="img" aria-label="Close-up of a woman's face with clear skin"></div>
  <div class="appt-info">
    <div class="appt-head"><small>YOUR</small><strong>Appointment</strong></div>
    <p class="lead">You need to be prepared when visiting the clinic before and after for skin rejuvenation.</p>
    <h2 class="contact-title">Contact Us</h2>
    <p class="contact-name">Maple Cove Laser Dermal Studio</p>
    <p class="contact-line">Harborview Medical Plaza<br>2040 Cedar Ridge Rd, Suite 12<br>Maple Cove, TX 70012</p>
    <p class="contact-line"><span class="lbl">Phone:</span><a href="tel:5553104827">(555) 310-4827</a></p>
    <p class="contact-line"><span class="lbl">Email:</span>info@maplecovelaserdermalstudio.com</p>
  </div>
  <form class="booking">
    <div class="row">
      <div class="field"><label>Your Name</label><div class="input"></div></div>
      <div class="field"><label>Your Email</label><div class="input"></div></div>
    </div>
    <div class="row">
      <div class="field"><label>Your Visit Date</label><div class="input"></div></div>
      <div class="field"><label>Your Visit Timing</label><div class="input"></div></div>
    </div>
    <div class="row">
      <div class="field"><label>Your Message</label><div class="area"></div></div>
    </div>
    <span class="btn">Book My Visit</span>
  </form>
</section>

<footer class="site-footer">
  <a class="brand" href="http://maplecovelaserdermalstudio.com"><span class="brand-mark"></span><span>Maple Cove Laser Dermal Studio</span></a>
  <nav class="foot-nav">
    <a href="#">About Us</a><i>/</i><a href="#">Skin Renewal</a><i>/</i><a href="#">Scar Removal</a><i>/</i><a href="#">Wart Removal</a><i>/</i><a href="#">Your Visit</a><i>/</i><a href="#">Contact Us</a><i>/</i><a href="#">Blog</a>
  </nav>
  <div class="foot-contact"><span class="lbl">Phone:</span> <a href="tel:5553104827">(555) 310-4827</a> &nbsp;<span class="lbl">Email:</span> info@maplecovelaserdermalstudio.com</div>
  <div class="copyright">© Copyright 2014 Maple Cove Laser Dermal Studio. All Rights Reserved.</div>
</footer>

</body>
</html>
```